Better Movement for Every Day
Project: Business Card & Letterhead
Business Card & Letterhead
Bright & Fun-filled
Dale Varnek
Strength & Conditioning Coach
42 Millbrook Lane Halden, VT 05744
dale@strideformlab.com
www.strideformlab.com
Whether competing on the field of play or in the game of life Stride Form Lab is your proven partner for: Performance Enhancement Injury Reduction & Rehabilitation Weight Management & Nutritional Strategies General Fitness Consulting to Companies and Schools Team Training

```html
<!DOCTYPE html>
<html lang="en">
<head>
<meta charset="utf-8">
<title>Stride Form Lab — Business Card</title>
<link href="https://fonts.googleapis.com/css2?family=Open+Sans:ital,wght@0,400;0,600;0,700;1,400&display=swap" rel="stylesheet">
<style>
  :root {
    --bg: #e8e9eb;
    --card-white: #ffffff;
    --brand-blue: #1f5fc4;
    --brand-blue-deep: #0f3f98;
    --brand-blue-light: #3d86e6;
    --charcoal: #2a2b2e;
    --charcoal-light: #4a4c50;
    --silver: #c9ccd1;
    --ink: #3a3c40;
    --ink-soft: #6b6e73;
  }
  * { margin: 0; padding: 0; box-sizing: border-box; }
  html, body { width: 1200px; height: 790px; overflow: hidden; }
  body {
    background: var(--bg);
    font-family: "Open Sans", Arial, sans-serif;
    position: relative;
  }
  .card {
    position: absolute;
    top: 252px;
    width: 500px;
    height: 286px;
    border-radius: 14px;
    overflow: hidden;
    box-shadow: 0 10px 28px rgba(0,0,0,0.22);
    background: var(--card-white);
  }
  .card--front { left: 70px; }
  .card--back { left: 630px; }
  .card__art { position: absolute; inset: 0; width: 100%; height: 100%; }

  .brand { position: absolute; text-align: center; }
  .brand__row { display: flex; align-items: center; justify-content: center; gap: 8px; }
  .brand__dot {
    width: 16px; height: 16px; border-radius: 50%;
    background: var(--brand-blue);
  }
  .brand__name {
    font-weight: 600; color: var(--brand-blue-deep);
    font-size: 21px; letter-spacing: -0.2px; white-space: nowrap;
  }
  .brand__tagline {
    font-style: italic; color: var(--brand-blue);
    font-size: 8.5px; margin-top: 2px; white-space: nowrap;
  }
  .card--front .brand { left: 26px; top: 118px; }
  .card--front .brand__row { justify-content: flex-start; }
  .card--front .brand__tagline { text-align: left; padding-left: 24px; }
  .card--back .brand { left: 0; right: 0; top: 112px; }
  .card--back .brand__name { font-size: 24px; }
  .card--back .brand__tagline { font-size: 9.5px; }

  .person { position: absolute; left: 268px; top: 72px; }
  .person__name { font-size: 15px; font-weight: 600; color: var(--brand-blue-deep); }
  .person__role { font-size: 9px; color: var(--ink-soft); margin-top: 1px; }

  .contacts { position: absolute; left: 268px; top: 134px; list-style: none; }
  .contacts__item {
    display: flex; align-items: center; gap: 6px;
    font-size: 8px; color: var(--ink); line-height: 1.2; margin-bottom: 5px;
  }
  .contacts__icon { width: 11px; height: 11px; flex: none; }
</style>
</head>
<body>

  <section class="card card--front" aria-label="Business card front">
    <svg class="card__art" viewBox="0 0 500 286" aria-hidden="true">
      <defs>
        <linearGradient id="frontBlue" x1="0" y1="0" x2="1" y2="1">
          <stop offset="0" stop-color="#3d86e6"/>
          <stop offset="1" stop-color="#0f3f98"/>
        </linearGradient>
        <linearGradient id="frontCharcoal" x1="0" y1="0" x2="1" y2="0">
          <stop offset="0" stop-color="#4a4c50"/>
          <stop offset="1" stop-color="#1e1f22"/>
        </linearGradient>
      </defs>
      <rect width="500" height="286" fill="url(#frontBlue)"/>
      <path d="M405 0 H500 V170 C494 95 462 38 405 0 Z" fill="url(#frontCharcoal)"/>
      <path d="M0 0 H395 C468 58 478 200 418 248 C338 292 120 276 0 262 Z" fill="#ffffff" stroke="#c9ccd1" stroke-width="4"/>
    </svg>

    <div class="brand">
      <div class="brand__row">
        <span class="brand__dot"></span>
        <span class="brand__name">Stride Form Lab</span>
      </div>
      <p class="brand__tagline">Better Movement for Every Day</p>
    </div>

    <div class="person">
      <p class="person__name">Dale Varnek</p>
      <p class="person__role">Strength &amp; Conditioning Coach</p>
    </div>

    <ul class="contacts">
      <li class="contacts__item">
        <svg class="contacts__icon" viewBox="0 0 12 12"><circle cx="6" cy="6" r="6" fill="#2a2b2e"/><path d="M6 2.5a2 2 0 0 0-2 2c0 1.6 2 4.5 2 4.5s2-2.9 2-4.5a2 2 0 0 0-2-2z" fill="#fff"/></svg>
        <span>42 Millbrook Lane<br>Halden, VT 05744</span>
      </li>
      <li class="contacts__item">
        <svg class="contacts__icon" viewBox="0 0 12 12"><circle cx="6" cy="6" r="6" fill="#2a2b2e"/><path d="M4 3h1.2l.6 1.5-.8.6a4 4 0 0 0 1.9 1.9l.6-.8L9 6.8V8a1 1 0 0 1-1 1A5 5 0 0 1 3 4a1 1 0 0 1 1-1z" fill="#fff"/></svg>
        <span>(555) 318-0142</span>
      </li>
      <li class="contacts__item">
        <svg class="contacts__icon" viewBox="0 0 12 12"><circle cx="6" cy="6" r="6" fill="#2a2b2e"/><rect x="3" y="4" width="6" height="4.2" fill="#fff"/><path d="M3 4l3 2.3L9 4" stroke="#2a2b2e" stroke-width=".7" fill="none"/></svg>
        <span>dale@strideformlab.com</span>
      </li>
      <li class="contacts__item">
        <svg class="contacts__icon" viewBox="0 0 12 12"><circle cx="6" cy="6" r="6" fill="#2a2b2e"/><circle cx="6" cy="6" r="3" stroke="#fff" stroke-width=".8" fill="none"/><path d="M3 6h6M6 3v6" stroke="#fff" stroke-width=".7"/></svg>
        <span>www.strideformlab.com</span>
      </li>
    </ul>
  </section>

  <section class="card card--back" aria-label="Business card back">
    <svg class="card__art" viewBox="0 0 500 286" aria-hidden="true">
      <defs>
        <linearGradient id="backCharcoal" x1="0" y1="0" x2="1" y2="1">
          <stop offset="0" stop-color="#4a4c50"/>
          <stop offset="1" stop-color="#1e1f22"/>
        </linearGradient>
        <linearGradient id="backBlue" x1="0" y1="0" x2="1" y2="1">
          <stop offset="0" stop-color="#3d86e6"/>
          <stop offset="1" stop-color="#0f3f98"/>
        </linearGradient>
      </defs>
      <rect width="500" height="286" fill="url(#backCharcoal)"/>
      <ellipse cx="232" cy="128" rx="250" ry="180" fill="url(#backBlue)"/>
      <ellipse cx="270" cy="160" rx="250" ry="180" fill="url(#backBlue)"/>
      <ellipse cx="252" cy="146" rx="236" ry="172" fill="#ffffff" stroke="#c9ccd1" stroke-width="4"/>
    </svg>

    <div class="brand">
      <div class="brand__row">
        <span class="brand__dot"></span>
        <span class="brand__name">Stride Form Lab</span>
      </div>
      <p class="brand__tagline">Better Movement for Every Day</p>
    </div>
  </section>

</body>
</html>
```